I need the following on my business card:
- Name: Dana Whitcomb
- License # 0M93216
- Title: Producer
- Phone: (555) 017-3904
- Email: Dana@CorbelInsuranceServices.com

- Company: Corbel Insurance Services
- Address: 27408 Larkmoor Ave Suite 610, Larkmoor Vale, CA 90217
- Website: www.CorbelInsuranceServices.com

Also add our slogan on the card: "Where Care Meets Confidence"

```html
<!DOCTYPE html>
<html lang="en">
<head>
<meta charset="utf-8">
<title>Corbel Insurance Services – Business Card</title>
<link rel="stylesheet" href="https://fonts.googleapis.com/css2?family=Montserrat:wght@400;500;600;700&family=Open+Sans:wght@400&display=swap">
<style>
  :root {
    --backdrop: #cfd4e8;
    --navy: #243473;
    --green: #12984a;
    --grey: #808080;
    --white: #ffffff;
  }
  * { margin: 0; padding: 0; box-sizing: border-box; }
  html, body { width: 1200px; height: 1200px; overflow: hidden; }
  body { background: var(--backdrop); position: relative; font-family: "Montserrat", sans-serif; }

  .card { position: absolute; left: 223px; width: 754px; height: 419px; overflow: hidden; }
  .card-front { top: 123px; background: var(--white); }
  .card-back { top: 633px; background: var(--navy); }

  .wordmark {
    position: absolute; font-family: "Montserrat", sans-serif; font-weight: 700;
    text-transform: uppercase; line-height: 1.15;
  }
  .card-front .wordmark { left: 19px; top: 206px; width: 275px; color: var(--navy); }
  .wordmark .wordmark-name { display: block; font-size: 40px; letter-spacing: 1px; }
  .wordmark .wordmark-sub { display: block; font-size: 13.4px; letter-spacing: 6.2px; }
  .card-back .wordmark { left: 0; right: 0; top: 186px; text-align: center; color: var(--white); }
  .card-back .wordmark .wordmark-name { font-size: 60px; }
  .card-back .wordmark .wordmark-sub { font-size: 21px; letter-spacing: 7.5px; margin-top: 4px; }

  .divider { position: absolute; left: 318px; width: 2px; }
  .divider-name { top: 87px; height: 58px; background: var(--navy); }
  .divider-details { top: 177px; height: 158px; background: var(--grey); }

  .person { position: absolute; left: 363px; top: 87px; }
  .person-name { font-size: 28px; font-weight: 600; color: var(--navy); text-transform: uppercase; line-height: 1.1; }
  .person-title { font-size: 21px; font-weight: 400; color: var(--grey); line-height: 1.3; }

  .company { position: absolute; left: 361px; top: 172px; }
  .company-name { font-size: 21px; font-weight: 600; color: var(--navy); line-height: 1.3; }
  .company-address { font-size: 20px; font-weight: 400; color: var(--grey); line-height: 1.32; }

  .contact-list { position: absolute; left: 361px; top: 261px; list-style: none; }
  .contact-item { display: flex; align-items: center; height: 26px; font-family: "Open Sans", sans-serif; font-size: 19px; color: var(--grey); }
  .contact-icon { width: 18px; height: 18px; margin-right: 15px; flex: none; }

  .footer-bands { position: absolute; left: 0; top: 0; width: 754px; height: 419px; }
  .license { position: absolute; left: 524px; top: 387px; font-size: 18.5px; font-weight: 600; color: var(--white); letter-spacing: 0.2px; }

  .slogan { position: absolute; left: 0; right: 0; top: 365px; text-align: center; color: var(--white); font-size: 17.5px; font-weight: 400; letter-spacing: 0.4px; text-transform: uppercase; }
</style>
</head>
<body>
  <section class="card card-front">
    <div class="wordmark"><span class="wordmark-name">Corbel</span><span class="wordmark-sub">Insurance Services</span></div>

    <span class="divider divider-name"></span>
    <div class="person">
      <p class="person-name">Dana Whitcomb</p>
      <p class="person-title">Producer</p>
    </div>

    <span class="divider divider-details"></span>
    <div class="company">
      <p class="company-name">Corbel Insurance Services</p>
      <p class="company-address">27408 Larkmoor Ave Suite 610<br>Larkmoor Vale, CA 90217</p>
    </div>

    <ul class="contact-list">
      <li class="contact-item">
        <svg class="contact-icon" viewBox="0 0 24 24"><path fill="var(--green)" d="M6.6 10.8c1.4 2.8 3.8 5.1 6.6 6.6l2.2-2.2c.3-.3.7-.4 1-.2 1.1.4 2.3.6 3.6.6.6 0 1 .4 1 1V20c0 .6-.4 1-1 1C10.6 21 3 13.4 3 4c0-.6.4-1 1-1h3.5c.6 0 1 .4 1 1 0 1.3.2 2.5.6 3.6.1.3 0 .7-.2 1L6.6 10.8z"/></svg>
        <span>(555) 017-3904</span>
      </li>
      <li class="contact-item">
        <svg class="contact-icon" viewBox="0 0 24 24"><rect x="2" y="5" width="20" height="14" fill="var(--green)"/><path d="M2 5l10 8 10-8M2 19l7-7M22 19l-7-7" stroke="var(--white)" stroke-width="1.6" fill="none"/></svg>
        <span>Dana@CorbelInsuranceServices.com</span>
      </li>
      <li class="contact-item">
        <svg class="contact-icon" viewBox="0 0 24 24" fill="none" stroke="var(--green)" stroke-width="1.8"><circle cx="12" cy="12" r="9.5"/><ellipse cx="12" cy="12" rx="4" ry="9.5"/><path d="M2.5 12h19M4 7h16M4 17h16"/></svg>
        <span>www.CorbelInsuranceServices.com</span>
      </li>
    </ul>

    <svg class="footer-bands" viewBox="0 0 754 419" aria-hidden="true">
      <polygon points="0,391 498,391 492,400 0,400" fill="var(--green)"/>
      <path d="M0 404 L496 404 Q502 404 506 398 L514 387 Q516 385 520 385 L754 385 L754 419 L0 419 Z" fill="var(--navy)"/>
    </svg>
    <p class="license">License # 0M93216</p>
  </section>

  <section class="card card-back">
    <div class="wordmark"><span class="wordmark-name">Corbel</span><span class="wordmark-sub">Insurance Services</span></div>
    <p class="slogan">Where Care Meets Confidence</p>
  </section>
</body>
</html>
```